Australian Skilled Migration

We need to design a add/flyer for a newspaper/magazine to promote our Australian Migration firm services. We targeting overseas graduating students and professionals who would like to Permanently Migrate to Australia.

We would like to advertise following services to our potential clients:

AUSTRALIA NEEDS YOU!!!

# Are you young and energetic individual?
# Do you have qualifications, work experiences or both?
# Perhaps you would like to open a small business, and sponsor yourself to live in Australia?
# Aspiring for job security and the highest living standards?

Contact us to find out how we can help you with Permanent Migration to Australia.

First consultation and eligibility assessment is free ! Tell your friends about us and receive a discount on your future fees!!

For more information please visit our website: www.corvintrak.org.au

(for a background we would like to use Australian themes such as: sandy beaches, ect... light colours)

Target Market(s)

Students
University graduates
Trade people with qualifications
Industry professionals
Anyone who wants to migrate to Australia

Industry/Entity Type

Security

Requirements
Must have
• our logo and website
easy to see and read the txt

Catchy Background
Nice to have
• as per our requirements
(designer questions, please e-mail: info@corvintrak.org. au)

```html
<!DOCTYPE html>
<html lang="en">
<head>
<meta charset="utf-8">
<title>Australia Needs You – Corvintrak &amp; Co</title>
<link href="https://fonts.googleapis.com/css2?family=Cormorant+Garamond:wght@500;600&family=Tinos:wght@700&family=Arimo:ital,wght@1,700&family=Crimson+Text:wght@600;700&display=swap" rel="stylesheet">
<style>
  :root {
    --backdrop: #2b2b2b;
    --sky-top: #5b86b8;
    --sky-mid: #c3d0dc;
    --sea: #2f6f8f;
    --sea-light: #6fa6b8;
    --sand: #c9a474;
    --sand-dark: #8f6f4f;
    --white: #ffffff;
    --teal-panel: rgba(38, 190, 210, 0.86);
    --amber-panel: rgba(228, 160, 62, 0.78);
    --ink: #1a1a1a;
    --brand-red: #d8261c;
  }
  html, body {
    margin: 0;
    padding: 0;
    width: 900px;
    height: 1200px;
    overflow: hidden;
    background: var(--backdrop);
  }
  .canvas {
    position: relative;
    width: 900px;
    height: 1200px;
    background: var(--backdrop);
  }
  .flyer {
    position: absolute;
    left: 60px;
    top: 60px;
    width: 778px;
    height: 1090px;
    overflow: hidden;
  }
  .flyer__scene {
    position: absolute;
    inset: 0;
    background: linear-gradient(180deg,
      var(--sky-top) 0%,
      var(--sky-mid) 22%,
      #d7dde2 34%,
      var(--sea-light) 46%,
      var(--sea) 56%,
      var(--sea-light) 66%,
      var(--sand) 76%,
      var(--sand-dark) 100%);
  }
  .headline {
    position: absolute;
    left: 0;
    width: 778px;
    margin: 0;
    text-align: center;
    font-family: "Cormorant Garamond", Georgia, serif;
    font-weight: 500;
    color: var(--white);
    text-shadow: 0 2px 6px rgba(0, 0, 0, 0.45);
    line-height: 1;
  }
  .headline--country { top: 72px; font-size: 118px; letter-spacing: 2px; }
  .headline--call { top: 172px; font-size: 100px; }

  .questions {
    position: absolute;
    left: 0;
    top: 305px;
    width: 740px;
    height: 255px;
    background: var(--teal-panel);
    margin: 0;
    padding: 40px 30px 0 47px;
    box-sizing: border-box;
    list-style: none;
    font-family: "Tinos", "Times New Roman", serif;
    font-weight: 700;
    font-size: 19.5px;
    line-height: 22px;
    color: var(--white);
  }
  .questions li {
    position: relative;
    padding-left: 26px;
    margin-bottom: 14px;
  }
  .questions li::before {
    content: "";
    position: absolute;
    left: 0;
    top: 6px;
    width: 10px;
    height: 10px;
    background: var(--white);
  }

  .contact-line {
    position: absolute;
    right: 33px;
    top: 586px;
    margin: 0;
    text-align: right;
    font-family: "Arimo", Arial, sans-serif;
    font-style: italic;
    font-weight: 700;
    font-size: 22.5px;
    line-height: 29px;
    color: var(--white);
    text-shadow: 0 1px 4px rgba(0, 0, 0, 0.6);
  }

  .offer {
    position: absolute;
    left: 105px;
    top: 680px;
    width: 673px;
    height: 108px;
    background: var(--amber-panel);
    padding: 6px 30px 0 0;
    box-sizing: border-box;
    text-align: right;
    font-family: "Crimson Text", Georgia, serif;
    font-weight: 700;
    font-size: 23px;
    line-height: 29px;
    color: var(--ink);
  }
  .offer p { margin: 0; }
  .offer__free { color: var(--white); }
  .offer__discount { color: var(--brand-red); font-size: 22px; }

  .brand {
    position: absolute;
    left: 185px;
    top: 880px;
    width: 560px;
    height: 160px;
  }
  .brand__mark {
    position: absolute;
    left: 0;
    top: 0;
  }
  .brand__name,
  .brand__tagline,
  .brand__web {
    position: absolute;
    left: 220px;
    margin: 0;
    font-family: "Crimson Text", Georgia, serif;
    font-weight: 700;
    color: var(--brand-red);
    white-space: nowrap;
  }
  .brand__name { top: 32px; font-size: 50px; line-height: 1; }
  .brand__tagline { top: 98px; font-size: 22px; }
  .brand__web { top: 132px; font-size: 19px; }
</style>
</head>
<body>
<main class="canvas">
  <article class="flyer">
    <div class="flyer__scene" role="img" aria-label="Photograph of a sandy Australian beach with limestone sea stacks, ocean surf and a cloudy blue sky"></div>

    <h1 class="headline headline--country">AUSTRALIA</h1>
    <p class="headline headline--call">Needs YOU!!!</p>

    <ul class="questions">
      <li>Are you young and energetic individual?</li>
      <li>Do you have qualifications, work experiences or both?</li>
      <li>Perhaps you would like to open a small business, and sponsor yourself to live in Australia?</li>
      <li>Aspiring for job security and the highest living standards?</li>
    </ul>

    <p class="contact-line">Contact us to find out how we can help you with<br>Permanent Migration to Australia</p>

    <section class="offer">
      <p>First consultation and eligibility assessment is <span class="offer__free">FREE !</span></p>
      <p>Tell your friends about us and</p>
      <p class="offer__discount">RECEIVE A DISCOUNT ON YOUR FUTURE FEES!!</p>
    </section>

    <footer class="brand">
      <svg class="brand__mark" width="190" height="160" viewBox="0 0 190 160" aria-hidden="true">
        <circle cx="95" cy="80" r="74" fill="none" stroke="#d8261c" stroke-width="4"/>
      </svg>
      <p class="brand__name">Corvintrak &amp; Co</p>
      <p class="brand__tagline">Lawyers &amp; Migration Agents</p>
      <p class="brand__web">www.corvintrak.org.au</p>
    </footer>
  </article>
</main>
</body>
</html>
```